Kessel Fahrwerkstatt
Sehr angenehme zusammenarbeit nicht aufdringlich und genau auf die Wünsche eingegangen. Wir werde sicher noch mehr zusammen Arbeiten. Gruss Lukas Hemmerle Inhaber Kessel Fahrwerkstatt
Zielgruppe
Dinks und Kunden mit viel Erfolg und hohem Ausgabepotential.
Aufgabenstellung
Unsere Firma vertreibt Fahrzeuge im Luxusbereich hauptgebiet Valtro aber auch andere Sportwagen. Was uns fehlt ist ein optischer Wiedererkennugswert. Deshalb hätten wir gerne ein Visitenkarten Design und Briefpapier Design. Später soll auch noch eine Webseite mit gleichem Wiedererkennungswert entstehen. " Roter Faden "

```html
<!DOCTYPE html>
<html lang="de">
<head>
<meta charset="utf-8">
<title>Kessel Fahrwerkstatt – Geschäftsausstattung</title>
<link rel="stylesheet" href="https://fonts.googleapis.com/css2?family=Arimo:wght@400;700&display=swap">
<style>
  :root {
    --stage: #000000;
    --paper: #ffffff;
    --red-deep: #3a0c10;
    --red-mid: #8e2326;
    --red-bright: #c94444;
    --shadow-grey: #4a4a4a;
    --text-light: #ffffff;
    --text-soft: #f1dede;
  }
  * { margin: 0; padding: 0; box-sizing: border-box; }
  html, body { width: 1200px; height: 900px; overflow: hidden; }
  body {
    background: var(--stage);
    font-family: "Arimo", Arial, sans-serif;
    color: var(--text-light);
    position: relative;
  }

  /* Letterhead */
  .letterhead {
    position: absolute; left: 47px; top: 50px;
    width: 465px; height: 650px;
    background: var(--paper);
    overflow: hidden;
  }
  .letterhead svg { position: absolute; inset: 0; }
  .letterhead .brand {
    position: absolute; left: 0; right: 0; top: 48px;
    text-align: center;
    font-size: 17px; font-weight: 700; letter-spacing: 2px;
    text-transform: uppercase;
  }
  .letterhead .web {
    position: absolute; right: 14px; top: 134px;
    font-size: 8px; letter-spacing: .5px; color: var(--text-light);
  }
  .letterhead .address {
    position: absolute; left: 20px; bottom: 18px;
    font-size: 9px; line-height: 14px;
  }
  .address b { font-weight: 700; }

  /* Name placement where the mark stood */
  .brand-display {
    position: absolute; left: 690px; top: 170px; width: 360px;
    text-align: center;
    font-size: 26px; font-weight: 700; letter-spacing: 2px;
    text-transform: uppercase; color: var(--text-light);
  }

  /* Business cards */
  .card {
    position: absolute; top: 463px;
    width: 285px; height: 188px; overflow: hidden;
    background:
      radial-gradient(ellipse 70% 45% at 50% 50%, rgba(214,90,90,.55), transparent 70%),
      linear-gradient(180deg, var(--red-deep) 0%, var(--red-mid) 30%, var(--red-bright) 50%, var(--red-mid) 70%, var(--red-deep) 100%);
  }
  .card-front { left: 546px; }
  .card-front .brand {
    position: absolute; left: 0; right: 0; top: 78px;
    text-align: center;
    font-size: 16px; font-weight: 700; letter-spacing: 2px;
    text-transform: uppercase;
  }
  .card-front .web {
    position: absolute; left: 0; right: 0; top: 104px;
    text-align: center; font-size: 11px; font-weight: 700; letter-spacing: 1.5px;
  }

  .card-back { left: 859px; }
  .card-back .strip {
    position: absolute; left: 0; top: 0; width: 78px; height: 100%;
    background: rgba(255,255,255,.14);
    border-right: 1px solid rgba(255,255,255,.18);
  }
  .card-back .strip-name {
    position: absolute; left: 30px; top: 94px;
    transform: translate(-50%, -50%) rotate(-90deg);
    white-space: nowrap;
    font-size: 11px; font-weight: 700; letter-spacing: 1.5px;
    text-transform: uppercase;
  }
  .card-back .person {
    position: absolute; left: 100px; top: 30px;
    font-size: 20px; font-weight: 400;
  }
  .contact-list {
    position: absolute; left: 100px; top: 66px; list-style: none;
    font-size: 13px; line-height: 17px;
  }
  .contact-list li { display: flex; align-items: center; gap: 8px; }
  .contact-list svg { width: 11px; height: 11px; flex: none; }
  .locations {
    position: absolute; left: 80px; top: 140px;
    display: flex; gap: 14px; font-size: 10.5px; line-height: 12px;
  }
  .locations b { display: block; font-weight: 700; }
</style>
</head>
<body>

  <section class="letterhead" aria-label="Briefpapier">
    <svg viewBox="0 0 465 650" width="465" height="650" aria-hidden="true">
      <defs>
        <linearGradient id="band-red" x1="0" y1="0" x2="0" y2="1">
          <stop offset="0" stop-color="#7a1d20"/>
          <stop offset=".45" stop-color="#c94444"/>
          <stop offset="1" stop-color="#6a1518"/>
        </linearGradient>
      </defs>
      <path d="M0 0H465V168C380 140 260 128 150 138C90 143 40 152 0 160Z" fill="url(#band-red)"/>
      <path d="M0 160C40 152 90 143 150 138C260 128 380 140 465 168V178C380 152 260 140 150 148C90 153 40 162 0 172Z" fill="var(--shadow-grey)"/>
      <path d="M0 602C110 582 280 570 465 560V650H0Z" fill="url(#band-red)"/>
      <path d="M0 594C110 574 280 562 465 552V560C280 570 110 582 0 602Z" fill="var(--shadow-grey)"/>
    </svg>
    <div class="brand">Kessel Fahrwerkstatt</div>
    <div class="web">www.kessel-fahrwerk.ch</div>
    <p class="address">
      <b>Büro :</b> Mühlegasse 12 - CH 8105 Talwil<br>
      <b>Showroom :</b> Seeweg 3 - CH 8620 Riedbach
    </p>
  </section>

  <div class="brand-display">Kessel Fahrwerkstatt</div>

  <section class="card card-front" aria-label="Visitenkarte Vorderseite">
    <div class="brand">Kessel Fahrwerkstatt</div>
    <div class="web">www.kessel-fahrwerk.ch</div>
  </section>

  <section class="card card-back" aria-label="Visitenkarte Rückseite">
    <div class="strip"></div>
    <div class="strip-name">Kessel Fahrwerkstatt</div>
    <div class="person">Lukas Hemmerle</div>
    <ul class="contact-list">
      <li>
        <svg viewBox="0 0 12 12" aria-hidden="true"><path d="M3 1h2l1 3-1.5 1a6 6 0 0 0 2.5 2.5L8 6l3 1v2a2 2 0 0 1-2 2A8 8 0 0 1 1 3a2 2 0 0 1 2-2z" fill="none" stroke="#fff" stroke-width="1"/></svg>
        +41 79 555 01 23
      </li>
      <li>
        <svg viewBox="0 0 12 12" aria-hidden="true"><rect x=".5" y="2.5" width="11" height="7" fill="none" stroke="#fff"/><path d="M.5 2.5 6 7l5.5-4.5" fill="none" stroke="#fff"/></svg>
        info@kessel-fahrwerk.ch
      </li>
      <li>
        <svg viewBox="0 0 12 12" aria-hidden="true"><rect x="2" y="2" width="8" height="6" fill="none" stroke="#fff"/><path d="M0.5 10h11" stroke="#fff" stroke-width="1.2"/></svg>
        www.kessel-fahrwerk.ch
      </li>
    </ul>
    <div class="locations">
      <div><b>Büro:</b>Mühlegasse 12<br>CH 8105 Talwil</div>
      <div><b>Showroom:</b>Seeweg 3<br>CH 8620 Riedbach</div>
    </div>
  </section>

</body>
</html>
```